Kestrel Gardenworks Business Card

An eye catching, yet simple business card that includes;

1. our logo
2. office phone - 5083172946
3. email - kestrelgardenworks@mailbrook.com
4. website - www.kestrelgardenworks.com
5. instagram - @kestrelgardenworksnv

```html
<!DOCTYPE html>
<html lang="en">
<head>
<meta charset="utf-8">
<title>Kestrel Gardenworks Business Card</title>
<link href="https://fonts.googleapis.com/css2?family=Montserrat:wght@300;400;700&display=swap" rel="stylesheet">
<style>
  :root {
    --ink: #29231f;
    --bronze: #ad733a;
    --paper: #ffffff;
    --label: #111111;
  }
  html, body {
    margin: 0;
    padding: 0;
    width: 1200px;
    height: 1200px;
    overflow: hidden;
    background: var(--paper);
  }
  .sheet {
    position: relative;
    width: 1200px;
    height: 1200px;
    font-family: "Montserrat", sans-serif;
  }
  .side-label {
    position: absolute;
    margin: 0;
    font-weight: 300;
    font-size: 44px;
    letter-spacing: 1px;
    color: var(--label);
    line-height: 1;
    transform: translateX(-50%);
  }
  .side-label--front { left: 272px; top: 258px; }
  .side-label--back  { left: 812px; top: 371px; }
  .card {
    position: absolute;
    display: block;
    outline: 1px solid var(--ink);
  }
  .card--front { left: 105px; top: 322px; width: 322px; height: 564px; }
  .card--back  { left: 539px; top: 442px; width: 564px; height: 323px; }
  .fill-ink { fill: var(--ink); }
  .fill-bronze { fill: var(--bronze); }
  .fill-paper { fill: var(--paper); }
  .brand-name {
    font-family: "Montserrat", sans-serif;
    font-weight: 700;
    fill: var(--ink);
  }
  .contact-line {
    font-family: "Montserrat", sans-serif;
    font-weight: 400;
    font-size: 30px;
    fill: var(--paper);
    letter-spacing: 0.5px;
  }
</style>
</head>
<body>
<main class="sheet">
  <h2 class="side-label side-label--front">FRONT</h2>
  <h2 class="side-label side-label--back">BACK</h2>

  <svg class="card card--front" viewBox="0 0 516 902" preserveAspectRatio="none" aria-label="Card front">
    <defs>
      <radialGradient id="artGlowFront" cx="0.45" cy="0.6" r="0.6">
        <stop offset="0" stop-color="#ad733a"/>
        <stop offset="0.6" stop-color="#ad733a" stop-opacity="0.55"/>
        <stop offset="1" stop-color="#29231f" stop-opacity="0"/>
      </radialGradient>
    </defs>
    <rect class="fill-ink" width="516" height="902"/>
    <path class="fill-bronze" d="M0 0 H516 V266 C400 330 220 322 110 252 C40 206 5 140 0 70 Z"/>
    <path class="fill-paper" d="M0 0 H516 V218 C400 282 220 286 110 222 C45 182 5 130 0 70 Z"/>
    <path class="fill-bronze" d="M0 358 C100 362 200 385 262 408 L258 410 C200 393 100 376 0 373 Z"/>
    <rect role="img" aria-label="Leaping kangaroo illustration in bronze" x="0" y="478" width="470" height="380" fill="url(#artGlowFront)"/>
    <text class="brand-name" x="300" y="120" font-size="54" text-anchor="middle">Kestrel</text>
    <text class="brand-name" x="300" y="178" font-size="40" text-anchor="middle">Gardenworks</text>
  </svg>

  <svg class="card card--back" viewBox="0 0 902 516" preserveAspectRatio="none" aria-label="Card back">
    <defs>
      <radialGradient id="artGlowBack" cx="0.6" cy="0.55" r="0.6">
        <stop offset="0" stop-color="#ad733a"/>
        <stop offset="0.6" stop-color="#ad733a" stop-opacity="0.55"/>
        <stop offset="1" stop-color="#29231f" stop-opacity="0"/>
      </radialGradient>
    </defs>
    <rect class="fill-ink" width="902" height="516"/>
    <path class="fill-bronze" d="M0 0 H410 C395 120 260 210 110 210 C70 210 30 203 0 195 Z"/>
    <path class="fill-paper" d="M0 0 H406 C380 105 260 170 130 170 C80 170 35 162 0 150 Z"/>
    <path class="fill-bronze" d="M698 68 C780 45 840 33 902 28 V40 C840 42 780 52 700 69 Z"/>
    <rect role="img" aria-label="Leaping kangaroo illustration in bronze" x="640" y="115" width="262" height="300" fill="url(#artGlowBack)"/>
    <text class="brand-name" x="148" y="84" font-size="42" text-anchor="middle">Kestrel</text>
    <text class="brand-name" x="148" y="126" font-size="30" text-anchor="middle">Gardenworks</text>
    <text class="contact-line" x="56" y="289">5083172946</text>
    <text class="contact-line" x="56" y="332">kestrelgardenworks@mailbrook.com</text>
    <text class="contact-line" x="56" y="375">www.kestrelgardenworks.com</text>
    <text class="contact-line" x="56" y="417">kestrelgardenworksnv</text>
  </svg>
</main>
</body>
</html>
```